Design concept Visual UI of future mobile app - healthcare

Hi,
I'm looking for a top designer, innovative with strong experience in user interface

The app will be connected to a future health website related to depression and addiction by helping the user to track the moods, tired, anxiety using this mobile app.

I attached the deck of the overall project but I can send you a specific presentation for the app only

thanks

Target Market(s)

Switzerland, UK, Germany and France

Industry/Entity Type

Mental Health

Logo Text

Health, hope

Font styles to use
Sans Serif

Colors
cee9f5
33a6d7
0692cd
0255a3
3276b5
85abd2

Requirements
Must have
• keep it simple, easy to navigate
• The user should be able to track the moods on a daily basis,
• sleep time, and rate how the feel on the day
• To be able to get information from the tally box of bront
Nice to have
• to be able share this app with a friend

```html
<!DOCTYPE html>
<html lang="en">
<head>
<meta charset="utf-8">
<title>Mood tracker app screens</title>
<link rel="stylesheet" href="https://fonts.googleapis.com/css2?family=Comfortaa:wght@300;400&family=Open+Sans:wght@400;700&display=swap">
<style>
:root{
  --ice:#cee9f5;
  --sky:#33a6d7;
  --azure:#0692cd;
  --navy:#0255a3;
  --body:#3276b5;
  --mist:#85abd2;
  --status:#8aa6e6;
  --title:#e3f0fa;
  --battery:#3fb64a;
  --page:#ffffff;
}
*{box-sizing:border-box;margin:0;padding:0}
html,body{width:1200px;height:737px;overflow:hidden;background:var(--page)}
.canvas{position:relative;width:1200px;height:737px;border:1px solid #1c3fd1}
.phone{position:absolute;width:145px;height:256px;background:var(--body);overflow:hidden;font-family:"Comfortaa",sans-serif}
.status{position:relative;height:12px;background:var(--status)}
.status .time{position:absolute;left:0;right:0;top:1px;text-align:center;font:700 8px/10px "Open Sans",sans-serif;color:#fff}
.status .signal{position:absolute;left:4px;top:3px}
.status .battery{position:absolute;right:4px;top:3px}
.header{height:27px;background:var(--navy)}
.avatar{position:absolute;left:104px;top:23px;width:32px;height:32px;border-radius:50%;background:var(--navy)}
.avatar svg{display:block}
.user{position:absolute;right:47px;top:41px;font-size:9px;font-weight:300;color:var(--mist)}
.title{position:absolute;left:0;width:100%;text-align:center;font-weight:300;color:var(--title);font-size:21px;line-height:1}
.title.small{font-size:15px;line-height:15px}
.rule{position:absolute;left:10px;width:125px;height:1px;background:linear-gradient(90deg,transparent,var(--ice) 50%,transparent)}
.rule.dark{background:linear-gradient(90deg,transparent,var(--navy) 30%,var(--navy) 70%,transparent)}
.menu-btn{position:absolute;left:0;width:100%;height:27px;background:var(--azure);color:#fff;text-align:center;font:400 10px/27px "Open Sans",sans-serif;font-variant:small-caps;letter-spacing:.2px}
.dots{position:absolute;left:0;width:100%;display:flex;justify-content:center;gap:9px}
.dots i{display:block;width:3px;height:3px;border-radius:50%;background:var(--mist)}
.dots i:first-child{background:#fff}
.legend{position:absolute;top:207px;left:18px;display:flex;gap:8px;font:400 9px/10px "Open Sans",sans-serif;color:#fff}
.legend span{display:flex;align-items:center;gap:2px}
.legend b{display:inline-block;width:10px;height:10px;border-radius:1px}
.note{position:absolute;left:15px;color:#fff;font:400 15px/17px "Open Sans",sans-serif}
.note::before{content:"";position:absolute;left:-9px;top:3px;width:4px;height:4px;border-radius:50%;background:#fff}
.social-row{position:absolute;left:15px;display:flex;align-items:center;gap:9px;font:400 8px/1 "Open Sans",sans-serif;color:var(--mist)}
.social-row b{display:block;width:15px;height:15px;background:#fff}
.setting-item{position:absolute;left:10px;font-size:12.5px;font-weight:300;color:var(--ice);letter-spacing:.4px}
</style>
</head>
<body>
<div class="canvas">

<!-- Home -->
<section class="phone" style="left:341px;top:102px">
  <div class="status"><svg class="signal" width="12" height="7"><rect x="0" y="4" width="2" height="3" fill="#fff"/><rect x="3" y="3" width="2" height="4" fill="#fff"/><rect x="6" y="1" width="2" height="6" fill="#fff"/><rect x="9" y="0" width="2" height="7" fill="#fff"/></svg><span class="time">19:20</span><svg class="battery" width="15" height="7"><rect x=".5" y=".5" width="12" height="6" fill="var(--battery)" stroke="#fff"/><rect x="13" y="2" width="2" height="3" fill="#fff"/></svg></div>
  <div class="header"></div>
  <div class="avatar"><svg width="32" height="32"><circle cx="16" cy="12" r="5" fill="var(--sky)"/><path d="M7 24a9 7 0 0 1 18 0z" fill="var(--sky)"/></svg></div>
  <span class="user">User Name</span>
  <h1 class="title" style="top:69px">Home</h1>
  <div class="rule" style="top:94px"></div>
  <div class="menu-btn" style="top:105px">Whats new today</div>
  <div class="menu-btn" style="top:140px">Tracking graphs</div>
  <div class="menu-btn" style="top:174px">Personal information</div>
</section>

<!-- Track -->
<section class="phone" style="left:527px;top:102px">
  <div class="status"><svg class="signal" width="12" height="7"><rect x="0" y="4" width="2" height="3" fill="#fff"/><rect x="3" y="3" width="2" height="4" fill="#fff"/><rect x="6" y="1" width="2" height="6" fill="#fff"/><rect x="9" y="0" width="2" height="7" fill="#fff"/></svg><span class="time">19:20</span><svg class="battery" width="15" height="7"><rect x=".5" y=".5" width="12" height="6" fill="var(--battery)" stroke="#fff"/><rect x="13" y="2" width="2" height="3" fill="#fff"/></svg></div>
  <div class="header"></div>
  <div class="avatar"><svg width="32" height="32"><circle cx="16" cy="12" r="5" fill="var(--sky)"/><path d="M7 24a9 7 0 0 1 18 0z" fill="var(--sky)"/></svg></div>
  <span class="user">User Name</span>
  <h1 class="title" style="top:72px">Track</h1>
  <div class="rule" style="top:97px"></div>
  <svg class="donut" style="position:absolute;left:32px;top:112px" width="80" height="80" viewBox="0 0 80 80">
    <g fill="none" stroke-width="11" transform="rotate(-90 40 40)">
      <circle cx="40" cy="40" r="33" stroke="#fff" stroke-dasharray="83 207"/>
      <circle cx="40" cy="40" r="33" stroke="var(--ice)" stroke-dasharray="0 83 62 207"/>
      <circle cx="40" cy="40" r="33" stroke="var(--azure)" stroke-dasharray="0 145 41 207"/>
      <circle cx="40" cy="40" r="33" stroke="var(--navy)" stroke-dasharray="0 186 21 207"/>
    </g>
  </svg>
  <div class="legend">
    <span><b style="background:#fff"></b>40%</span>
    <span><b style="background:var(--ice)"></b>30%</span>
    <span style="color:var(--sky)"><b style="background:var(--sky)"></b>20%</span>
  </div>
  <div class="dots" style="top:231px"><i></i><i></i><i></i></div>
</section>

<!-- Activity check-in -->
<section class="phone" style="left:695px;top:102px">
  <div class="status"><svg class="signal" width="12" height="7"><rect x="0" y="4" width="2" height="3" fill="#fff"/><rect x="3" y="3" width="2" height="4" fill="#fff"/><rect x="6" y="1" width="2" height="6" fill="#fff"/><rect x="9" y="0" width="2" height="7" fill="#fff"/></svg><span class="time">19:20</span><svg class="battery" width="15" height="7"><rect x=".5" y=".5" width="12" height="6" fill="var(--battery)" stroke="#fff"/><rect x="13" y="2" width="2" height="3" fill="#fff"/></svg></div>
  <div class="header"></div>
  <div class="avatar"><svg width="32" height="32"><circle cx="16" cy="12" r="5" fill="var(--sky)"/><path d="M7 24a9 7 0 0 1 18 0z" fill="var(--sky)"/></svg></div>
  <span class="user">User Name</span>
  <h1 class="title small" style="top:73px">Activity<br>Check-in</h1>
  <div class="rule" style="top:110px"></div>
  <svg class="sliders" style="position:absolute;left:0;top:120px" width="145" height="95">
    <g stroke-width="2">
      <line x1="22" y1="8" x2="123" y2="8" stroke="var(--navy)"/><line x1="22" y1="8" x2="39" y2="8" stroke="var(--mist)"/>
      <line x1="22" y1="27" x2="123" y2="27" stroke="var(--navy)"/><line x1="22" y1="27" x2="57" y2="27" stroke="var(--mist)"/>
      <line x1="22" y1="47" x2="123" y2="47" stroke="var(--navy)"/><line x1="22" y1="47" x2="72" y2="47" stroke="var(--mist)"/>
      <line x1="22" y1="66" x2="123" y2="66" stroke="var(--navy)"/><line x1="22" y1="66" x2="94" y2="66" stroke="var(--mist)"/>
      <line x1="22" y1="86" x2="123" y2="86" stroke="var(--navy)"/><line x1="22" y1="86" x2="117" y2="86" stroke="#dfe9f4"/>
    </g>
    <g fill="#bcd6f5">
      <circle cx="39" cy="8" r="4.5"/><circle cx="57" cy="27" r="4.5"/><circle cx="72" cy="47" r="4.5"/><circle cx="94" cy="66" r="4.5"/><circle cx="117" cy="86" r="4.5"/>
    </g>
  </svg>
  <div class="dots" style="top:231px"><i></i><i></i><i></i></div>
</section>

<!-- Message -->
<section class="phone" style="left:274px;top:378px">
  <div class="status"><svg class="signal" width="12" height="7"><rect x="0" y="4" width="2" height="3" fill="#fff"/><rect x="3" y="3" width="2" height="4" fill="#fff"/><rect x="6" y="1" width="2" height="6" fill="#fff"/><rect x="9" y="0" width="2" height="7" fill="#fff"/></svg><span class="time">19:20</span><svg class="battery" width="15" height="7"><rect x=".5" y=".5" width="12" height="6" fill="var(--battery)" stroke="#fff"/><rect x="13" y="2" width="2" height="3" fill="#fff"/></svg></div>
  <div class="header"></div>
  <div class="avatar"><svg width="32" height="32"><circle cx="16" cy="12" r="5" fill="var(--sky)"/><path d="M7 24a9 7 0 0 1 18 0z" fill="var(--sky)"/></svg></div>
  <span class="user">User Name</span>
  <h1 class="title" style="top:72px">Message</h1>
  <div class="rule" style="top:96px"></div>
  <p class="note" style="top:103px">Lorem ipsum<br>dolor sit amet,</p>
  <div class="rule dark" style="top:154px"></div>
  <p class="note" style="top:163px">Lorem ipsum<br>dolor sit amet,</p>
  <div class="rule dark" style="top:213px"></div>
  <div class="dots" style="top:230px"><i></i><i></i><i></i></div>
</section>

<!-- Social -->
<section class="phone" style="left:442px;top:378px">
  <div class="status"><svg class="signal" width="12" height="7"><rect x="0" y="4" width="2" height="3" fill="#fff"/><rect x="3" y="3" width="2" height="4" fill="#fff"/><rect x="6" y="1" width="2" height="6" fill="#fff"/><rect x="9" y="0" width="2" height="7" fill="#fff"/></svg><span class="time">19:20</span><svg class="battery" width="15" height="7"><rect x=".5" y=".5" width="12" height="6" fill="var(--battery)" stroke="#fff"/><rect x="13" y="2" width="2" height="3" fill="#fff"/></svg></div>
  <div class="header"></div>
  <div class="avatar"><svg width="32" height="32"><circle cx="16" cy="12" r="5" fill="var(--sky)"/><path d="M7 24a9 7 0 0 1 18 0z" fill="var(--sky)"/></svg></div>
  <span class="user">User Name</span>
  <h1 class="title" style="top:72px">Social</h1>
  <div class="rule" style="top:96px"></div>
  <div class="social-row" style="top:110px"><b></b>Connect to Pagemate</div>
  <div class="social-row" style="top:128px"><b></b>Connect to Chirpline</div>
  <div class="social-row" style="top:147px"><b></b>Connect to Orbitplus</div>
  <div class="social-row" style="top:166px"><b></b>Connect to Tackwall</div>
  <div class="social-row" style="top:184px"><b></b>Connect to Portfolix</div>
  <div class="social-row" style="top:202px"><b></b>Connect to Workring</div>
</section>

<!-- Setting -->
<section class="phone" style="left:610px;top:378px">
  <div class="status"><svg class="signal" width="12" height="7"><rect x="0" y="4" width="2" height="3" fill="#fff"/><rect x="3" y="3" width="2" height="4" fill="#fff"/><rect x="6" y="1" width="2" height="6" fill="#fff"/><rect x="9" y="0" width="2" height="7" fill="#fff"/></svg><span class="time">19:20</span><svg class="battery" width="15" height="7"><rect x=".5" y=".5" width="12" height="6" fill="var(--battery)" stroke="#fff"/><rect x="13" y="2" width="2" height="3" fill="#fff"/></svg></div>
  <div class="header"></div>
  <div class="avatar"><svg width="32" height="32"><circle cx="16" cy="12" r="5" fill="var(--sky)"/><path d="M7 24a9 7 0 0 1 18 0z" fill="var(--sky)"/></svg></div>
  <span class="user">User Name</span>
  <h1 class="title" style="top:72px">Setting</h1>
  <div class="rule" style="top:96px"></div>
  <span class="setting-item" style="top:108px">Profile</span>
  <div class="rule dark" style="top:126px"></div>
  <span class="setting-item" style="top:135px">Account</span>
  <div class="rule dark" style="top:154px"></div>
  <span class="setting-item" style="top:162px">Notification</span>
  <div class="rule dark" style="top:181px"></div>
  <span class="setting-item" style="top:189px">About</span>
  <div class="rule dark" style="top:208px"></div>
</section>

<!-- Invite a friend -->
<section class="phone" style="left:780px;top:378px">
  <div class="status"><svg class="signal" width="12" height="7"><rect x="0" y="4" width="2" height="3" fill="#fff"/><rect x="3" y="3" width="2" height="4" fill="#fff"/><rect x="6" y="1" width="2" height="6" fill="#fff"/><rect x="9" y="0" width="2" height="7" fill="#fff"/></svg><span class="time">19:20</span><svg class="battery" width="15" height="7"><rect x=".5" y=".5" width="12" height="6" fill="var(--battery)" stroke="#fff"/><rect x="13" y="2" width="2" height="3" fill="#fff"/></svg></div>
  <div class="header"></div>
  <div class="avatar"><svg width="32" height="32"><circle cx="16" cy="12" r="5" fill="var(--sky)"/><path d="M7 24a9 7 0 0 1 18 0z" fill="var(--sky)"/></svg></div>
  <span class="user">User Name</span>
  <h1 class="title small" style="top:72px">Invite<br><span style="display:inline-block;margin-top:2px">a Friend</span></h1>
  <div class="rule" style="top:110px"></div>
  <svg class="share-ring" style="position:absolute;left:0;top:0" width="145" height="256">
    <polygon points="71,130 102,149 103,184 72,201 41,184 41,149" fill="none" stroke="var(--ice)" stroke-width=".8"/>
    <g fill="var(--navy)">
      <circle cx="71" cy="130" r="9"/><circle cx="102" cy="149" r="9"/><circle cx="103" cy="184" r="9"/>
      <circle cx="72" cy="201" r="9"/><circle cx="41" cy="184" r="9"/><circle cx="41" cy="149" r="9"/>
      <circle cx="71" cy="166" r="13"/>
    </g>
    <g fill="none" stroke="#fff" stroke-width=".9">
      <rect x="36" y="145.5" width="10" height="7" rx=".5"/><path d="M36 146l5 3.5 5-3.5"/>
    </g>
    <circle cx="71" cy="162" r="3.5" fill="#fff"/>
    <path d="M64.5 172a6.5 5 0 0 1 13 0z" fill="#fff"/>
  </svg>
</section>

</div>
</body>
</html>
```